Brightwire Hollow Business cards

one side I would like my logo (uploaded) and the other side I want my details. I'm an electrician in sydney. The logo side I'm happy with just a white background and our logo in the middle.

Details for other side
24/7 Sydney Electrician
Marcus Pell
0431 587 219
marcus@brightwirehollow.com.au
brightwirehollow.com.au
icons for facebook, instagram, linked in

Industry/Entity Type

electrician

Contact Information for Business Card

company info

```html
<!DOCTYPE html>
<html lang="en">
<head>
<meta charset="utf-8">
<title>Brightwire Hollow – Business Cards</title>
<link href="https://fonts.googleapis.com/css2?family=Roboto:wght@400;500;700;900&display=swap" rel="stylesheet">
<style>
  :root {
    --stage: #3b3b3b;
    --card-dark: #262626;
    --card-light: #ffffff;
    --red: #e3261f;
    --black: #111111;
    --ink: #333333;
    --muted: #8a8a8a;
    --emboss-hi: #9a9a9a;
    --rule: #cfcfcf;
  }
  * { box-sizing: border-box; margin: 0; padding: 0; }
  html, body { width: 1200px; height: 689px; overflow: hidden; }
  body {
    background: var(--stage);
    font-family: "Roboto", Arial, sans-serif;
    position: relative;
  }
  .card {
    position: absolute;
    top: 195px;
    width: 520px;
    height: 300px;
    border-radius: 16px;
    overflow: hidden;
    box-shadow: 0 18px 40px rgba(0,0,0,.45);
  }

  /* Logo side */
  .card--logo { left: 40px; background: var(--card-dark); }
  .card--logo .brand {
    position: absolute; top: 96px; left: 0; width: 100%;
    text-align: center;
    font-weight: 900; font-size: 44px; letter-spacing: 1px;
    color: var(--emboss-hi);
    text-transform: uppercase;
  }
  .card--logo .tagline {
    position: absolute; top: 196px; left: 0; width: 100%;
    display: flex; justify-content: center; align-items: center; gap: 10px;
    color: #e8e8e8; font-size: 15px; font-weight: 500;
  }
  .badge {
    width: 26px; height: 26px; border-radius: 50%;
    border: 2px solid var(--red);
  }

  /* Details side */
  .card--details { left: 640px; background: var(--card-light); }
  .card--details .brand {
    position: absolute; left: 26px; top: 112px;
    width: 220px;
    font-weight: 900; font-size: 26px; line-height: 1.05;
    color: var(--red);
    text-transform: uppercase; letter-spacing: .5px;
  }
  .divider {
    position: absolute; left: 258px; top: 88px;
    width: 1px; height: 104px; background: var(--rule);
  }
  .contact { position: absolute; left: 278px; top: 92px; }
  .contact .name { font-size: 24px; font-weight: 700; color: var(--red); line-height: 1; }
  .contact .role { font-size: 12px; color: var(--muted); margin-top: 5px; }
  .contact .line {
    display: flex; align-items: center; gap: 8px;
    font-size: 13px; color: var(--ink); margin-top: 8px;
  }
  .contact .line:first-of-type { margin-top: 14px; }
  .contact .line svg { width: 12px; height: 12px; flex: none; }
  .icon-phone { fill: var(--red); }
  .icon-mail { fill: none; stroke: var(--red); stroke-width: 2.5; }
  .social {
    position: absolute; top: 20px; right: 22px; display: flex; gap: 6px;
  }
  .social span { width: 20px; height: 20px; border-radius: 50%; background: var(--red); }
  .band { position: absolute; left: 0; bottom: 0; width: 520px; height: 74px; }
  .website {
    position: absolute; right: 22px; bottom: 18px;
    color: #fff; font-size: 14px; font-weight: 500;
  }
</style>
</head>
<body>
  <section class="card card--logo">
    <div class="brand">Brightwire Hollow</div>
    <div class="tagline"><span class="badge"></span>Sydney Electrician</div>
  </section>

  <section class="card card--details">
    <div class="social" aria-label="Social media">
      <span></span><span></span><span></span>
    </div>
    <div class="brand">Brightwire<br>Hollow</div>
    <div class="divider"></div>
    <div class="contact">
      <div class="name">Marcus Pell</div>
      <div class="role">President</div>
      <div class="line">
        <svg class="icon-phone" viewBox="0 0 24 24"><path d="M6.6 10.8a15 15 0 0 0 6.6 6.6l2.2-2.2a1 1 0 0 1 1-.25 11.4 11.4 0 0 0 3.6.57 1 1 0 0 1 1 1V20a1 1 0 0 1-1 1A17 17 0 0 1 3 4a1 1 0 0 1 1-1h3.5a1 1 0 0 1 1 1c0 1.25.2 2.45.57 3.57a1 1 0 0 1-.25 1z"/></svg>
        0431 587 219
      </div>
      <div class="line">
        <svg class="icon-mail" viewBox="0 0 24 24"><path d="M2 5h20v14H2z M2 5l10 8 10-8"/></svg>
        marcus@brightwirehollow.com.au
      </div>
    </div>
    <svg class="band" viewBox="0 0 520 74" preserveAspectRatio="none" aria-hidden="true">
      <polygon points="0,54 250,54 282,22 288,22 256,58 0,58" fill="var(--black)"/>
      <polygon points="0,64 260,64 296,26 520,26 520,74 0,74" fill="var(--red)"/>
    </svg>
    <div class="website">www.brightwirehollow.com.au</div>
  </section>
</body>
</html>
```